Brochure and Banner Designs

We need to put the attached brochure in a very professional, intriguing and relaxing to read and interest follow up...we would like to work with the colours of our logo...the brown stands for healthy homes, the blue for engaged communities and the green for natural surroundings. We bought the pic in the brochure. We would like to see the kid with the puff in a transparent background to minimize distraction. Also we would like the picture to blend beautifully with the background. We have used a template with an idea if what we are looking for.

We also need a banner design. I have attached the idea as well. I also attached the logo of the company so you can play with ideas around it. The 3d pic is not final, we will receive it next week, for now lets leave the space for it and work on the look and the information...we thought about add the colours that belong to each pillar as indicated in the paragraph above. It could be kind of abstract...blending each colour in the transition...Please note that I included a closer pic of the buildings, since it could be blended with the aerial view. As indicated before the aerial view is draft for now.

Any way good lock and I will asssit all your questions....

Lucia
Updates

Please note that for the banner, we were advised that people will only have 3 seconds to see it (sicne they will be driving)...so to simplify the message, it was suggested removing the description under each pillar...so lets only leave:

Maison saines
Collectivité bienveillante
Cadre de vie naturel

Thanks,
Lucia

Please when write Le Verger on the top of the banner, please ensure is written as the file I just attached to the fiel for your information.

Hi, everyone...

                                 

Thanks for your time and ideas!

Lucia

Hi, Guys

Could you please confirm who is planning to submit designs..?

Thanks,

Lucia

I hope to receive more designs...

Lucia

                                       

1058924 Preferred front cover (only comment too beige) and center as for the family suggested the building behind the family and replaced the kids by the family in this design.

The vision and mission exchange position with the Do you know…for this page suggested removing the kid with the puff and using the asthma kid as a backgrounder as it is done in design 1066529 but only covering this page and making the asthma puff more evident. This will provide more space for text in that page. The vision and mission as design 1066529.

Proactive Approach on center inside line to be removed…so on the top of this page Healthy Homes..pics are preferred squared..

The engaged community pic has been change for the grandpa with kids around. Attached in the file.

As for the banner, it is considered too blue…please follow the background use for brochure cover for design 1058924. As for the website only use tormelio.com do not write tormelio twice. Pleas edo not use bullets for the elements…

Thanks for your participation!

Lucia

                                   

the tree as a background is vey nice...

Target Market(s)

Highly educated people specially women 35-55 years old $70K plus salaries

Industry/Entity Type

It Company

Requirements
Must have
• The logo
All the info included in the attachements...ideas are welcome on the language, structure, flow, colours, etc...
Nice to have
• Nice flow...focus points.
Should not have
• non earth colours

```html
<!DOCTYPE html>
<html lang="en">
<head>
<meta charset="utf-8">
<title>Tormelio – Healthy Living Communities Brochure (outside)</title>
<link rel="stylesheet" href="https://fonts.googleapis.com/css2?family=Arimo:wght@400&family=Cabin:wght@400&family=Marcellus&display=swap">
<style>
  :root {
    --stage: #e9e9e6;
    --cream: #f7f1cf;
    --cream-light: #fbf8e6;
    --mint: #9fd1a7;
    --mint-deep: #86c597;
    --sand: #e6d69a;
    --text: #3a3a34;
    --heading-green: #2c7a4b;
    --brown: #6b3f17;
    --brown-soft: #8b5a2b;
    --leaf: #a9cc5a;
  }
  * { box-sizing: border-box; margin: 0; padding: 0; }
  html, body { width: 1200px; height: 900px; overflow: hidden; }
  body {
    background: var(--stage);
    font-family: "Arimo", Arial, sans-serif;
    color: var(--text);
    position: relative;
  }
  .brochure {
    position: absolute;
    left: 52px; top: 28px;
    width: 1096px; height: 844px;
    display: grid;
    grid-template-columns: 362px 370px 364px;
  }
  .panel { position: relative; overflow: hidden; }

  /* Mission panel */
  .panel--mission {
    background:
      radial-gradient(ellipse 90% 45% at 0% 100%, var(--mint-deep) 0%, rgba(159,209,167,0.6) 45%, rgba(159,209,167,0) 80%),
      linear-gradient(90deg, var(--mint) 0%, #cfe6b6 25%, var(--cream) 55%, var(--cream-light) 100%);
    text-align: center;
    padding: 52px 52px 0 60px;
  }
  .mission-title {
    font-family: "Marcellus", "Optima", serif;
    font-weight: 400;
    color: var(--heading-green);
    font-size: 33px;
    line-height: 40px;
    margin-bottom: 30px;
  }
  .mission-text {
    font-size: 19.5px;
    line-height: 24.5px;
    margin-bottom: 38px;
  }

  /* Contact panel */
  .panel--contact {
    background:
      radial-gradient(ellipse 55% 40% at 50% 40%, #c6dc7a 0%, rgba(198,220,122,0.55) 45%, rgba(230,236,180,0) 80%),
      linear-gradient(180deg, #f3f1cb 0%, #eef0c8 50%, #f4f3d9 100%);
    text-align: center;
    border-left: 1px solid #f7f5e4;
    border-right: 1px solid #f2eed0;
  }
  .brand {
    position: absolute; left: 0; right: 0; top: 352px;
    display: flex; align-items: center; justify-content: center; gap: 14px;
  }
  .brand-dot {
    width: 22px; height: 22px; border-radius: 50%;
    background: var(--leaf);
  }
  .brand-name {
    font-family: "Cabin", sans-serif;
    font-weight: 400;
    font-size: 64px;
    line-height: 1;
    color: var(--brown);
  }
  .tagline {
    position: absolute; left: 0; right: 0; top: 444px;
    font-family: "Cabin", sans-serif;
    font-weight: 400;
    font-size: 21px;
    color: var(--brown-soft);
  }
  .address {
    position: absolute; left: 0; right: 0; top: 508px;
    font-style: normal;
    font-size: 19.5px;
    line-height: 24.5px;
    color: var(--text);
  }
  .website {
    position: absolute; left: 0; right: 0; top: 686px;
    font-family: "Cabin", sans-serif;
    font-weight: 400;
    font-size: 27px;
    color: var(--brown-soft);
  }

  /* Cover panel */
  .panel--cover {
    background: linear-gradient(180deg, #f1e6b6 0%, var(--sand) 45%, #ece0ae 75%, #f3ecd2 100%);
  }
  .cover-curves { position: absolute; inset: 0; }
  .cover-photo {
    position: absolute; left: 6px; top: 96px;
    width: 346px; height: 224px;
    border-radius: 48% 48% 40% 40% / 50% 50% 30% 30%;
    background: radial-gradient(ellipse at 50% 45%, #d9c3a8 0%, #c9b9a4 35%, #d8d7cf 60%, rgba(241,230,182,0) 78%);
  }
  .cover-title {
    position: absolute; left: 34px; top: 478px;
    font-family: "Marcellus", "Optima", serif;
    font-weight: 400;
    font-variant: small-caps;
    font-size: 54px;
    line-height: 62px;
    color: var(--brown);
    text-shadow: 1px 1px 1px rgba(120,90,40,0.25);
  }
</style>
</head>
<body>
  <main class="brochure">
    <section class="panel panel--mission">
      <h2 class="mission-title">Our Mission</h2>
      <p class="mission-text">To develop healthy residential communities that infuse life with vitality by nurturing the mind, body and soul.</p>
      <p class="mission-text">Behind this mission is a desire to address the unprecedented challenges of our times.</p>
      <p class="mission-text">Our deep conviction to effecting real change, our collective understanding of the paramount role of relationships to health, and our complementary experience in business, technical, and large scale infrastructure capacities, have been instrumental in creating what we trust is a truly inspiring and empowering model of healthy living communities.</p>
    </section>

    <section class="panel panel--contact">
      <div class="brand">
        <span class="brand-dot"></span>
        <span class="brand-name">tormelio</span>
      </div>
      <p class="tagline">Healthy, Living Communities</p>
      <address class="address">
        1485 Rue des Érables<br>
        PO 62170 Belmont<br>
        Gatineau&nbsp; QC<br>
        J8R 4M2<br>
        819-555-0187<br>
        info@tormelio.com
      </address>
      <p class="website">www.tormelio.com</p>
    </section>

    <section class="panel panel--cover">
      <svg class="cover-curves" viewBox="0 0 364 844" preserveAspectRatio="none" aria-hidden="true">
        <path d="M0 470 C 120 380, 260 400, 364 470 L364 844 L0 844 Z" fill="#efe5b8" opacity="0.55"/>
        <path d="M0 640 C 110 560, 250 600, 364 700 L364 844 L0 844 Z" fill="#f5efd6" opacity="0.6"/>
        <path d="M120 844 C 200 760, 290 740, 364 760 L364 844 Z" fill="#f8f4e2" opacity="0.7"/>
      </svg>
      <div class="cover-photo" role="img" aria-label="Photo of a smiling multi-generation family sitting together: grandparents, parents and two children"></div>
      <h1 class="cover-title">Healthy<br>Living<br>Communities</h1>
    </section>
  </main>
</body>
</html>
```